依頼詳細
PC版のTOPページと下層1ページ(採用情報)のデザイン制作をお願いいたします。
サイトマップ、依頼内容詳細.txtをご確認いただき、動画のテイストを参考にシンプルで見やすいデザインで制作いただきたいです。
スムーズな連絡と軽微な修正にご対応いただける方へご依頼をさせていただきたいです。
ターゲットは木材資材・建築資材・家具建具資材などを必要とする建築会社様、家具・建具製造会社様などです。
ページ数
2ページ
希望イメージ
シンプル 複雑
単色 カラフル
暗い 明るい
日常 高級
遊び心 厳粛
未来的 伝統的
女性的 男性的
希望する色
茶系、緑系、グレー系
納品ファイル
• イラストレーター形式 (.ai)
補足説明
納品ファイルはXDも可です。
添付してあるアニメーションにテイストを合わせ、
木の温かみを感じさせるデザインで制作してください。
コーポレートですが、あまり堅くなり過ぎないようにしたいです。
BtoB向けの会社ではありますが、就職などを考えている若い方が見ても、
面白そうな企業だなという印象も与えたいです。
動画ダウンロードURLを新たに添付いたしましたので
そちらからダウンロードをお願い致します。
■ 選んだ理由

爽やかな緑を使ったデザインが良かったです。

■ 提案者全員のお礼・コメント

たくさんのご提案をいただきありがとうございました。

```html
<!DOCTYPE html>
<html lang="ja">
<head>
<meta charset="utf-8">
<title>KITAMORI TIMBER</title>
<link href="https://fonts.googleapis.com/css2?family=Montserrat:wght@400;500;600;700&family=Noto+Sans+JP:wght@400;500;700&display=swap" rel="stylesheet">
<style>
:root{
  --green:#1f7a1f;
  --green-dark:#176317;
  --ink:#222;
  --muted:#555;
  --line:#d8d8d8;
  --pale:#eef3ec;
  --white:#fff;
}
*{margin:0;padding:0;box-sizing:border-box}
html,body{width:1200px;height:4648px;overflow:hidden;background:var(--white)}
body{font-family:"Noto Sans JP",sans-serif;color:var(--ink);position:relative}
.en{font-family:"Montserrat",sans-serif}
section,header,footer{position:absolute;left:0;width:1200px;overflow:hidden}

/* header */
.site-header{top:0;height:56px;border-bottom:1px solid var(--line);background:var(--white)}
.site-header .brand{position:absolute;left:24px;top:16px;font:600 22px "Montserrat",sans-serif;letter-spacing:1px}
.site-header nav{position:absolute;right:110px;top:21px;display:flex;gap:26px;font-size:13px;font-weight:500}
.menu-btn{position:absolute;right:0;top:0;width:56px;height:56px;background:#111;display:flex;flex-direction:column;justify-content:center;align-items:center;gap:6px}
.menu-btn span{display:block;width:22px;height:2px;background:var(--white)}

/* hero */
.hero{top:56px;height:616px;background:var(--white)}
.hero .tree-left{position:absolute;left:0;top:40px;width:520px;height:560px;background:radial-gradient(ellipse at 40% 35%,#8fc46d 0%,#c6e2b0 40%,rgba(255,255,255,0) 70%)}
.hero .tree-right{position:absolute;right:0;top:120px;width:520px;height:496px;background:radial-gradient(ellipse at 60% 35%,#8fc46d 0%,#c6e2b0 40%,rgba(255,255,255,0) 70%)}
.hero h1{position:absolute;left:100px;top:330px;font:600 104px/1.05 "Montserrat",sans-serif;letter-spacing:4px;color:#111}
.hero h1 span{display:block}
.hero h1 span+span{padding-left:40px}

/* section heading */
.label{display:inline-block;background:var(--green);color:var(--white);font:700 46px/1 "Montserrat",sans-serif;padding:8px 14px 6px;letter-spacing:1px}
.label-sub{display:block;margin-top:6px;width:max-content;background:var(--green);color:var(--white);font-size:11px;padding:2px 6px}
.view-more{display:flex;align-items:center;gap:14px;font:600 12px "Montserrat",sans-serif;letter-spacing:1px}
.view-more .circle{width:64px;height:64px;border:1px solid #333;border-radius:50%;display:flex;align-items:center;justify-content:center;margin-left:-30px;position:relative}
.view-more .circle::before{content:"";position:absolute;left:-2px;top:31px;width:36px;height:1px;background:#333}

/* greenting */
.greenting{top:672px;height:576px;border-top:1px solid var(--line)}
.greenting .photo{position:absolute;left:0;top:0;width:600px;height:576px;background:linear-gradient(160deg,#5f7f3c,#2e4a22 55%,#6b5a3c)}
.greenting .body{position:absolute;left:672px;top:120px;width:440px}
.greenting p{margin-top:32px;font-size:13px;line-height:2;color:var(--muted)}
.greenting .view-more{margin-top:48px}
.greenting .sapling{position:absolute;right:60px;bottom:24px;width:110px;height:140px;background:radial-gradient(ellipse at 50% 30%,#7fb85a,rgba(255,255,255,0) 65%)}

/* news */
.news{top:1248px;height:512px;border-top:1px solid var(--line)}
.news .head{position:absolute;left:120px;top:120px}
.news ul{position:absolute;left:360px;top:124px;width:720px;list-style:none}
.news li{display:flex;gap:40px;padding:20px 0;border-bottom:1px solid var(--line);font-size:13px}
.news time{font-family:"Montserrat",sans-serif;font-weight:500}
.news .view-more{position:absolute;left:366px;top:370px}

/* business */
.business{top:1760px;height:960px;border-top:1px solid var(--line)}
.business .pale{position:absolute;left:0;top:0;width:600px;height:960px;background:var(--pale)}
.business .head{position:absolute;left:120px;top:132px}
.business .cards{position:absolute;left:120px;top:260px;display:flex;gap:16px}
.biz-card{width:524px}
.biz-card .photo{height:420px;position:relative}
.biz-card .cap{position:absolute;left:0;bottom:0;background:#111;color:var(--white);font-size:12px;padding:8px 12px}
.biz-card p{margin-top:12px;font-size:13px;line-height:1.9;color:var(--muted)}
.business .view-more{position:absolute;left:126px;top:760px}

/* product */
.product{top:2720px;height:860px;border-top:1px solid var(--line)}
.product .head{position:absolute;left:120px;top:132px}
.product .arrows{position:absolute;right:120px;top:148px;display:flex;gap:14px}
.product .arrows span{width:60px;height:60px;border:1px solid #999;border-radius:50%;display:flex;align-items:center;justify-content:center}
.product .cards{position:absolute;left:120px;top:248px;display:flex;gap:16px}
.prod-card{width:292px}
.prod-card .photo{height:292px;position:relative}
.prod-card .cap{position:absolute;left:0;bottom:0;background:#111;color:var(--white);font-size:12px;padding:6px 12px}
.prod-card p{margin-top:12px;font-size:13px;line-height:1.9;color:var(--muted)}
.product .view-more{position:absolute;left:126px;top:690px}

/* recruit */
.recruit{top:3580px;height:560px;background:linear-gradient(135deg,#4b4036,#7a6a58 45%,#3a3a36)}
.recruit .body{position:absolute;left:120px;top:176px;color:var(--white)}
.recruit h2{font:600 56px "Montserrat",sans-serif;letter-spacing:1px}
.recruit .sub{font-size:12px}
.recruit .note{margin-top:22px;display:flex;flex-direction:column;gap:6px;align-items:flex-start}
.recruit .note span{background:var(--white);color:var(--ink);font-size:14px;font-weight:700;padding:4px 10px}

/* contact */
.contact{top:4140px;height:260px;background:var(--green);color:var(--white);text-align:center}
.contact h2{margin-top:90px;font:600 44px "Montserrat",sans-serif;letter-spacing:1px}
.contact p{font-size:13px;margin-top:4px}
.contact .circle{position:absolute;right:70px;top:98px;width:64px;height:64px;border:1px solid var(--white);border-radius:50%}
.contact .circle::before{content:"";position:absolute;left:-26px;top:31px;width:56px;height:1px;background:var(--white)}

/* footer */
.site-footer{top:4400px;height:248px;border-top:1px solid var(--line)}
.site-footer .brand{position:absolute;left:56px;top:78px;font:600 24px "Montserrat",sans-serif;letter-spacing:1px}
.site-footer ul{position:absolute;top:70px;list-style:none;font-size:13px;line-height:2.3}
.site-footer .col1{left:760px}
.site-footer .col2{left:940px}
</style>
</head>
<body>

<header class="site-header">
  <div class="brand">KITAMORI TIMBER</div>
  <nav><span>会社概要</span><span>事業内容</span><span>取扱商品</span><span>採用情報</span></nav>
  <div class="menu-btn"><span></span><span></span><span></span></div>
</header>

<section class="hero">
  <div class="tree-left" role="img" aria-label="緑の葉と赤い実をつけた木のイラスト"></div>
  <div class="tree-right" role="img" aria-label="緑の葉と赤い実をつけた木のイラスト"></div>
  <h1><span>KITAMORI</span><span>TIMBER</span></h1>
</section>

<section class="greenting">
  <div class="photo" role="img" aria-label="苔むした大木の幹と枝を見上げた写真"></div>
  <div class="body">
    <div class="label">GREENTING</div>
    <span class="label-sub">ご挨拶</span>
    <p>北杜木材株式会社は、銘木、家具、建築資材の取扱いを通じて、木の温もりを大切に届けることを使命としています。<br><br>人と木材の新しい出会いを日々創造しています。<br>北の森から、次の世代へ、新しい価値を発信します。</p>
    <div class="view-more">VIEW MORE<span class="circle"></span></div>
  </div>
  <div class="sapling" role="img" aria-label="小さな木のイラスト"></div>
</section>

<section class="news">
  <div class="head"><div class="label">NEWS</div><span class="label-sub">お知らせ</span></div>
  <ul>
    <li><time>2021.02.24</time><span>ここにお知らせのテキストが入ります。ダミーテキストです。</span></li>
    <li><time>2021.02.24</time><span>ここにお知らせのテキストが入ります。ダミーテキストです。</span></li>
    <li><time>2021.02.24</time><span>ここにお知らせのテキストが入ります。ダミーテキストです。</span></li>
  </ul>
  <div class="view-more">VIEW MORE<span class="circle"></span></div>
</section>

<section class="business">
  <div class="pale"></div>
  <div class="head"><div class="label">OUR BUSINESS</div><span class="label-sub">事業内容</span></div>
  <div class="cards">
    <div class="biz-card">
      <div class="photo" role="img" aria-label="木目の内装が広がる店舗空間の写真" style="background:linear-gradient(160deg,#5a4a3a,#2c2620 60%,#8a6a48)"><span class="cap">木材資材・家具資材・建具資材の販売</span></div>
      <p>ここに木材資材・家具資材・建具資材の販売のテキストが入ります。ダミーテキストです。</p>
    </div>
    <div class="biz-card">
      <div class="photo" role="img" aria-label="夕暮れに灯る木造住宅の外観写真" style="background:linear-gradient(170deg,#3e4a5a,#6b6256 55%,#2a2a26)"><span class="cap">住宅建材・構造材・化粧材の販売</span></div>
      <p>ここに住宅建材・構造材・化粧材の販売のテキストが入ります。ダミーテキストです。</p>
    </div>
  </div>
  <div class="view-more">VIEW MORE<span class="circle"></span></div>
</section>

<section class="product">
  <div class="head"><div class="label">PRODUCT</div><span class="label-sub">取扱商品</span></div>
  <div class="arrows">
    <span><svg width="16" height="16" viewBox="0 0 16 16"><path d="M10 2 L4 8 L10 14" fill="none" stroke="#999" stroke-width="1.5"/></svg></span>
    <span><svg width="16" height="16" viewBox="0 0 16 16"><path d="M6 2 L12 8 L6 14" fill="none" stroke="#333" stroke-width="1.5"/></svg></span>
  </div>
  <div class="cards">
    <div class="prod-card">
      <div class="photo" role="img" aria-label="断熱材に触れる手元の写真" style="background:linear-gradient(150deg,#c9a470,#e2c999)"><span class="cap">断熱材</span></div>
      <p>ここに断熱材のテキストが入ります。ダミーテキストです。</p>
    </div>
    <div class="prod-card">
      <div class="photo" role="img" aria-label="建築中の木造住宅の骨組み写真" style="background:linear-gradient(170deg,#8fb3d6,#c7a678 60%,#8a6a48)"><span class="cap">木構造建材</span></div>
      <p>ここに木構造建材のテキストが入ります。ダミーテキストです。</p>
    </div>
    <div class="prod-card">
      <div class="photo" role="img" aria-label="木の床が広がる明るい室内の写真" style="background:linear-gradient(170deg,#e6e2da,#b08a60)"><span class="cap">化粧材</span></div>
      <p>ここに化粧材のテキストが入ります。ダミーテキストです。</p>
    </div>
    <div class="prod-card">
      <div class="photo" role="img" aria-label="木の家具が並ぶ室内の写真" style="background:linear-gradient(170deg,#d8d4cc,#8a7258)"><span class="cap">外装材</span></div>
      <p>ここに外装材のテキストが入ります。ダミーテキストです。</p>
    </div>
  </div>
  <div class="view-more">VIEW MORE<span class="circle"></span></div>
</section>

<section class="recruit" role="img" aria-label="観葉植物と木の家具が置かれたオフィスの写真">
  <div class="body">
    <h2>RECRUIT</h2>
    <span class="sub">採用情報</span>
    <div class="note"><span>ここに採用情報のテキストが入ります。</span><span>ダミーテキストです。</span></div>
  </div>
</section>

<section class="contact">
  <h2>CONTACT</h2>
  <p>お問い合わせはこちら</p>
  <span class="circle"></span>
</section>

<footer class="site-footer">
  <div class="brand">KITAMORI TIMBER</div>
  <ul class="col1"><li>会社概要</li><li>取扱商品</li><li>メーカーリンク集</li><li>会員登録フォーム</li></ul>
  <ul class="col2"><li>事業情報一覧</li><li>採用情報</li><li>お問い合わせ</li><li>プライバシーポリシー</li></ul>
</footer>

</body>
</html>
```